Pop-up Banner

Would like a design for a pop-up 85 x 206cm banner for a trade show. (from norla press)
We would like "our logo" (brightwave holdings) - then the tagline - "Your Trusted Partner in Data-Driven Decisions"
*Supporting Bullets*
Unified data, analytics & AI
Trusted insights, faster outcomes
Real-time intelligence at scale
Enterprise-ready, secure solutions
Clarity from data complexity
trusted by...some company logos
Partners with : partner logo
Our Colours: #FFA300, #3D4176, #FDD16E, #F87C57, #A68118, #1C2F36

```html
<!DOCTYPE html>
<html lang="en">
<head>
<meta charset="utf-8">
<title>Brightwave Holdings – Pop-up Banner</title>
<link href="https://fonts.googleapis.com/css2?family=Roboto:wght@400;500;700;900&display=swap" rel="stylesheet">
<style>
  :root {
    --navy: #23267a;
    --indigo: #3d4176;
    --lavender: #8c88c4;
    --lavender-soft: #c9c6e6;
    --orange: #ffa300;
    --orange-deep: #e8901a;
    --gold: #fdd16e;
    --ink: #1c2f36;
    --paper: #fbfbfe;
    --stage: #eceef3;
    --muted: #6b6f8f;
  }
  * { box-sizing: border-box; margin: 0; padding: 0; }
  html, body { width: 1200px; height: 900px; overflow: hidden; }
  body { background: var(--stage); font-family: "Roboto", sans-serif; color: var(--navy); }

  .banner {
    position: absolute; left: 423px; top: 20px;
    width: 354px; height: 860px;
    background: var(--paper);
    overflow: hidden;
    box-shadow: 0 6px 24px rgba(30, 35, 80, .18);
  }
  .banner-shapes { position: absolute; inset: 0; }

  .brand {
    position: absolute; left: 52px; top: 112px;
    display: flex; align-items: center; gap: 12px;
  }
  .brand-mark { width: 46px; height: 46px; border-radius: 50%; background: var(--navy); }
  .brand-name {
    font-weight: 700; font-size: 21px; line-height: 1.05;
    letter-spacing: .06em; text-transform: uppercase; color: var(--navy);
  }

  .tagline { position: absolute; left: 0; right: 0; top: 200px; text-align: center; }
  .tagline-lead { font-weight: 700; font-size: 27px; color: var(--navy); }
  .tagline-key { font-weight: 900; font-size: 58px; line-height: 1; color: var(--orange-deep); letter-spacing: .01em; }
  .tagline-tail { font-weight: 700; font-size: 22px; color: var(--navy); margin-top: 4px; }

  .benefits { position: absolute; left: 28px; right: 26px; top: 356px; list-style: none; }
  .benefit {
    position: relative; display: flex; align-items: center; gap: 10px;
    height: 62px; font-size: 16.5px; font-weight: 500; color: var(--ink);
  }
  .benefit + .benefit::before {
    content: ""; position: absolute; left: 0; right: 0; top: 0;
    border-top: 1px solid var(--orange);
  }
  .benefit + .benefit::after {
    content: ""; position: absolute; left: 0; top: -1px;
    width: 16px; height: 3px; background: var(--indigo);
  }
  .benefit-icon { width: 30px; height: 33px; flex: none; }

  .proof-title {
    position: absolute; font-weight: 700; font-size: 17px;
    color: var(--indigo); letter-spacing: .02em; text-transform: uppercase;
  }
  .proof-title.trusted { left: 28px; top: 676px; font-size: 20px; color: var(--muted); }
  .proof-title.partners { left: 190px; top: 680px; }

  .proof-list { position: absolute; list-style: none; }
  .proof-list.trusted { left: 24px; top: 714px; width: 150px; display: flex; flex-wrap: wrap; gap: 8px 12px; }
  .proof-list.partners { left: 188px; top: 716px; display: flex; flex-direction: column; gap: 9px; }
  .proof-name { font-size: 13px; font-weight: 500; color: var(--indigo); white-space: nowrap; }
  .proof-list.partners .proof-name { font-size: 17px; display: flex; align-items: center; gap: 6px; }
  .proof-dot { width: 11px; height: 11px; background: var(--orange-deep); flex: none; }
</style>
</head>
<body>
  <main class="banner">
    <svg class="banner-shapes" viewBox="0 0 354 860" aria-hidden="true">
      <defs>
        <linearGradient id="lav" x1="0" y1="0" x2="1" y2="1">
          <stop offset="0" stop-color="#7d79bb"/>
          <stop offset="1" stop-color="#c9c6e6"/>
        </linearGradient>
        <linearGradient id="lavBottom" x1="1" y1="0" x2="0" y2="1">
          <stop offset="0" stop-color="#9e9ad0"/>
          <stop offset="1" stop-color="#d9d7ee"/>
        </linearGradient>
      </defs>
      <!-- top right corner -->
      <path d="M110 0 H354 V178 C330 96 262 30 110 0 Z" fill="var(--navy)"/>
      <path d="M140 6 C258 26 330 92 354 182" fill="none" stroke="var(--orange-deep)" stroke-width="9"/>
      <path d="M120 18 C240 36 318 100 346 198" fill="none" stroke="var(--indigo)" stroke-width="2.5"/>
      <!-- top left swoosh -->
      <path d="M0 32 C50 20 110 14 168 20 C80 50 22 122 0 232 Z" fill="url(#lav)"/>
      <!-- bottom right -->
      <path d="M354 640 C344 748 290 806 186 832 C250 840 310 846 354 848 Z" fill="url(#lavBottom)"/>
      <!-- bottom left -->
      <path d="M0 690 C26 790 130 846 300 860 H0 Z" fill="var(--navy)"/>
      <path d="M0 680 C30 782 140 840 354 852" fill="none" stroke="var(--gold)" stroke-width="7"/>
      <path d="M0 664 C34 770 150 832 354 846" fill="none" stroke="var(--indigo)" stroke-width="2" opacity=".7"/>
      <path d="M354 852 V860 H300 C320 857 340 855 354 852 Z" fill="var(--navy)"/>
      <!-- divider between trusted and partners -->
      <path d="M110 820 C160 790 168 730 178 698 C188 668 232 652 354 662" fill="none" stroke="var(--navy)" stroke-width="2.5"/>
    </svg>

    <header class="brand">
      <span class="brand-mark"></span>
      <span class="brand-name">Brightwave<br>Holdings</span>
    </header>

    <section class="tagline">
      <p class="tagline-lead">Your Trusted</p>
      <p class="tagline-key">Partner</p>
      <p class="tagline-tail">in Data-Driven Decisions</p>
    </section>

    <ul class="benefits">
      <li class="benefit">
        <svg class="benefit-icon" viewBox="0 0 30 33"><path d="M15 1 L29 9 V24 L15 32 L1 24 V9 Z" fill="var(--navy)"/><rect x="10" y="11" width="10" height="10" fill="none" stroke="#fff" stroke-width="1.6"/><path d="M12 8v3M18 8v3M12 21v3M18 21v3M7 14h3M7 18h3M20 14h3M20 18h3" stroke="#fff" stroke-width="1.3"/></svg>
        Unified data, analytics &amp; AI
      </li>
      <li class="benefit">
        <svg class="benefit-icon" viewBox="0 0 30 33"><path d="M15 1 L29 9 V24 L15 32 L1 24 V9 Z" fill="var(--navy)"/><circle cx="14" cy="15" r="5.5" fill="none" stroke="#fff" stroke-width="1.8"/><path d="M18 19 L22 23" stroke="#fff" stroke-width="2"/></svg>
        Trusted insights, faster outcomes
      </li>
      <li class="benefit">
        <svg class="benefit-icon" viewBox="0 0 30 33"><path d="M15 1 L29 9 V24 L15 32 L1 24 V9 Z" fill="var(--lavender)"/><circle cx="15" cy="16.5" r="7" fill="none" stroke="#fff" stroke-width="1.6"/><path d="M15 12v5l3 2" stroke="#fff" stroke-width="1.5" fill="none"/></svg>
        Real-time intelligence at scale
      </li>
      <li class="benefit">
        <svg class="benefit-icon" viewBox="0 0 30 33"><path d="M15 1 L29 9 V24 L15 32 L1 24 V9 Z" fill="var(--lavender)"/><path d="M15 9 L21 11.5 V16 C21 20 18 23 15 24 C12 23 9 20 9 16 V11.5 Z" fill="none" stroke="#fff" stroke-width="1.6"/><rect x="12.5" y="15" width="5" height="4" fill="#fff"/></svg>
        Enterprise-ready, secure solutions
      </li>
      <li class="benefit">
        <svg class="benefit-icon" viewBox="0 0 30 33"><path d="M15 1 L29 9 V24 L15 32 L1 24 V9 Z" fill="var(--lavender)"/><rect x="8" y="10" width="5" height="4" fill="none" stroke="#fff" stroke-width="1.4"/><rect x="17" y="14.5" width="5" height="4" fill="none" stroke="#fff" stroke-width="1.4"/><rect x="8" y="19" width="5" height="4" fill="none" stroke="#fff" stroke-width="1.4"/><path d="M13 12h2v9h-2M15 16.5h2" stroke="#fff" stroke-width="1.3" fill="none"/></svg>
        Clarity from data complexity
      </li>
    </ul>

    <h2 class="proof-title trusted">Trusted by</h2>
    <ul class="proof-list trusted">
      <li class="proof-name">Harbourline</li>
      <li class="proof-name">Kestrel</li>
      <li class="proof-name">Orvilo</li>
      <li class="proof-name">Quillfield</li>
      <li class="proof-name">Arden</li>
    </ul>

    <h2 class="proof-title partners">Partners with</h2>
    <ul class="proof-list partners">
      <li class="proof-name"><span class="proof-dot"></span>Lumacore</li>
      <li class="proof-name">Veridan</li>
      <li class="proof-name">clearpath systems</li>
      <li class="proof-name">Tallyworks</li>
    </ul>
  </main>
</body>
</html>
```